Business Card - Cooperate

Business Card for Larkfield Management Consulting

Target Market(s)

Corparte - b2B

Industry/Entity Type

Management Consulting - Professional Services

Contact Information for Business Card

Company Name , Slogan , Dummy Address,

Requirements
Must have
• Reach your Full Potential

```html
<!DOCTYPE html>
<html lang="en">
<head>
<meta charset="utf-8">
<title>Larkfield Management Consulting – Business Card</title>
<link href="https://fonts.googleapis.com/css2?family=Arimo:wght@400;700&display=swap" rel="stylesheet">
<style>
  :root {
    --backdrop: #c9d0d8;
    --card-white: #f7f7f7;
    --card-black: #050505;
    --ink: #111111;
    --brand-blue: #3d5bb8;
    --slogan-teal: #1f9c8a;
    --light-text: #f2f2f2;
  }
  * { box-sizing: border-box; margin: 0; padding: 0; }
  html, body { width: 1200px; height: 675px; overflow: hidden; }
  body {
    background: var(--backdrop);
    font-family: "Arimo", Arial, sans-serif;
    position: relative;
  }
  .card {
    position: absolute;
    width: 525px;
    height: 300px;
    border-radius: 3px;
    box-shadow: 0 10px 28px rgba(30, 40, 55, 0.25);
    overflow: hidden;
  }
  .card--front { left: 45px; top: 188px; background: var(--card-white); color: var(--ink); }
  .card--back  { left: 630px; top: 188px; background: var(--card-black); }

  .brand { position: absolute; display: flex; align-items: center; gap: 12px; }
  .brand__dot { width: 40px; height: 40px; border-radius: 50%; background: var(--brand-blue); flex: none; }
  .brand__name { font-size: 38px; font-weight: 700; color: var(--brand-blue); letter-spacing: 0.5px; line-height: 1; }
  .brand__slogan { font-size: 8.5px; font-weight: 700; color: var(--slogan-teal); letter-spacing: 2.6px; margin-top: 5px; }

  .card--front .brand { right: 40px; top: 38px; }

  .holder { position: absolute; left: 0; top: 110px; display: flex; align-items: flex-start; }
  .holder__bar { width: 16px; height: 38px; background: var(--ink); margin-right: 24px; margin-top: 6px; }
  .holder__name { font-size: 19px; font-weight: 700; letter-spacing: 0.3px; }
  .holder__role { font-size: 12px; margin-left: 6px; margin-top: 2px; }

  .address { position: absolute; left: 40px; top: 190px; font-size: 12px; line-height: 1.5; }
  .contact { position: absolute; font-size: 12.5px; line-height: 1.9; }
  .contact--phones { left: 40px; top: 236px; }
  .contact--online { right: 40px; top: 182px; }
  .contact__row { display: flex; align-items: center; gap: 10px; }
  .contact__row svg { width: 12px; height: 12px; flex: none; }

  .card--back .brand { left: 100px; top: 108px; }
  .website {
    position: absolute; left: 100px; top: 212px;
    color: var(--light-text); font-size: 14px; letter-spacing: 9px;
  }
</style>
</head>
<body>

<section class="card card--front" aria-label="Business card front">
  <div class="brand">
    <span class="brand__dot"></span>
    <div>
      <div class="brand__name">Larkfield</div>
      <div class="brand__slogan">REACH YOUR FULL POTENTIAL</div>
    </div>
  </div>

  <div class="holder">
    <span class="holder__bar"></span>
    <div>
      <div class="holder__name">YOUR NAME</div>
      <div class="holder__role">Manager</div>
    </div>
  </div>

  <div class="address">
    <div>Rua das Acácias, 48</div>
    <div>Edificio Aurora - Vale Verde</div>
  </div>

  <div class="contact contact--phones">
    <div class="contact__row">
      <svg viewBox="0 0 12 12" aria-hidden="true"><path d="M1 4c0-2 2-3 5-3s5 1 5 3l-2 .5-.5-1.5h-5L3 4.5z M2 6h8l1 5H1z" fill="#111"/></svg>
      <span>(123) 444-5555</span>
    </div>
    <div class="contact__row">
      <svg viewBox="0 0 12 12" aria-hidden="true"><rect x="3" y="0.5" width="6" height="3" fill="#111"/><rect x="0.5" y="4" width="11" height="5" rx="1" fill="#111"/><rect x="3" y="7.5" width="6" height="4" fill="#fff" stroke="#111"/></svg>
      <span>(123) 444-5556</span>
    </div>
  </div>

  <div class="contact contact--online">
    <div class="contact__row">
      <svg viewBox="0 0 12 12" aria-hidden="true"><rect x="0.5" y="2" width="11" height="8" fill="#111"/><path d="M0.5 2.5 6 7l5.5-4.5" fill="none" stroke="#fff"/></svg>
      <span>mail@yourmail.com</span>
    </div>
    <div class="contact__row">
      <svg viewBox="0 0 12 12" aria-hidden="true"><circle cx="6" cy="6" r="5.2" fill="none" stroke="#111" stroke-width="1.2"/><ellipse cx="6" cy="6" rx="2.2" ry="5.2" fill="none" stroke="#111"/><path d="M1 6h10M2 3.5h8M2 8.5h8" stroke="#111"/></svg>
      <span>www.yoursite.com</span>
    </div>
  </div>
</section>

<section class="card card--back" aria-label="Business card back">
  <div class="brand">
    <span class="brand__dot"></span>
    <div>
      <div class="brand__name">Larkfield</div>
      <div class="brand__slogan">REACH YOUR FULL POTENTIAL</div>
    </div>
  </div>
  <div class="website">www.yoursite.com</div>
</section>

</body>
</html>
```